Poster design for a company operating care homes in the UK showcasing our core values

We need a poster to display in our care homes showcasing our new core values:

Purpose
We are driven by a clear understanding of why we do what we do: to enrich lives, honour legacies and make a meaningful difference every day, for our residents, their families, our colleagues and our community.

Excellence
We hold ourselves to the highest standards, delivering exceptional care and creating an environment where both residents and staff can thrive.

Openness
We build trust through honest, respectful communication, welcoming feedback, sharing ideas, and embracing change as a path to continuous growth.

Passion
We are passionate about delivering exceptional care. We take pride in what we do and in making a real difference in people’s lives.

Learning
We are committed to personal and professional growth; empowering each other through ongoing development, reflection, and shared knowledge.

Empathy
We actively listen and seek to understand before being understood, recognising the unique stories, feelings, and needs of others.

I have attached a small graphic that we would like you try to incorporate, in addition to our company logo. Please theme the rest of the poster around our company colours.

```html
<!DOCTYPE html>
<html lang="en">
<head>
<meta charset="utf-8">
<title>Our Core Values – Solenne</title>
<link rel="stylesheet" href="https://fonts.googleapis.com/css2?family=Anton&family=Open+Sans:wght@400;700&family=Passion+One:wght@700&display=swap">
<style>
  :root{
    --navy:#1b2c48;
    --blue:#3a5374;
    --blue-light:#5a7ca8;
    --peach:#efa887;
    --peach-dark:#e2916c;
    --brown:#7a5346;
    --paper:#ececec;
    --panel:#e8e8e8;
    --ink:#1e1e1e;
    --white:#ffffff;
  }
  *{margin:0;padding:0;box-sizing:border-box}
  html,body{width:1200px;height:893px;overflow:hidden}
  body{background:var(--paper)}
  .poster{
    position:relative;width:1200px;height:893px;overflow:hidden;
    background:linear-gradient(125deg,#f3f3f3 0%,#e4e4e4 30%,#efefef 45%,#e2e2e2 70%,#f1f1f1 100%);
    font-family:"Open Sans",sans-serif;
  }
  .title-band{position:absolute;left:0;top:70px;width:1010px;height:183px}
  .title{
    position:absolute;left:60px;top:84px;
    font-family:"Anton",sans-serif;font-size:130px;line-height:1;letter-spacing:1px;
    color:var(--peach);white-space:nowrap;
  }
  .title .lead{color:var(--white)}
  .value{position:absolute;top:282px;width:170px;height:460px}
  .value .frame{position:absolute;left:0;top:18px;width:170px;height:380px}
  .value .badge{
    position:absolute;left:47px;top:0;width:76px;height:76px;border-radius:50%;
    background:var(--white);border:6px solid var(--blue);
    display:flex;align-items:center;justify-content:center;
    box-shadow:0 2px 4px rgba(0,0,0,.25);
  }
  .value.warm .badge{border-color:var(--peach)}
  .badge-core{width:54px;height:54px;border-radius:50%;background:var(--navy);display:flex;align-items:center;justify-content:center}
  .value.warm .badge-core{background:var(--peach-dark)}
  .badge-core svg{width:32px;height:32px}
  .value .text{
    position:absolute;left:24px;top:98px;width:122px;
    font-size:11.6px;line-height:15.6px;text-align:center;color:var(--ink);
  }
  .value .text strong{font-weight:700}
  .value .label{
    position:absolute;left:4px;top:393px;width:172px;height:54px;display:flex;
    color:var(--white);font-family:"Passion One",sans-serif;font-size:27px;
  }
  .label .initial{width:34px;display:flex;align-items:center;justify-content:center;font-size:40px}
  .label .rest{flex:1;display:flex;align-items:center;padding-left:8px}
  .value.warm .label .rest{color:var(--navy)}
  .footer-brand{position:absolute;left:66px;top:793px;display:flex;align-items:center;gap:12px}
  .footer-brand .mark{width:34px;height:34px;background:var(--peach)}
  .footer-brand .name{font-family:"Open Sans",sans-serif;font-weight:700;font-size:34px;color:var(--blue);letter-spacing:1px}
  .divider{position:absolute;left:348px;top:768px;width:2px;height:93px;background:var(--navy)}
  .web{
    position:absolute;left:378px;top:772px;
    font-family:"Anton",sans-serif;font-size:72px;line-height:1.2;color:var(--navy);white-space:nowrap;
  }
</style>
</head>
<body>
<div class="poster">
  <svg class="title-band" viewBox="0 0 1010 183" aria-hidden="true">
    <polygon points="0,0 920,0 1010,183 0,183" fill="var(--navy)"/>
  </svg>
  <h1 class="title"><span class="lead">our</span> core values</h1>

  <div class="value cool" style="left:58px">
    <svg class="frame" viewBox="0 0 170 380"><g fill="var(--blue)"><polygon points="15,8 155,8 155,38 15,38"/><rect x="0" y="45" width="12" height="230"/><rect x="158" y="45" width="12" height="230"/><polygon points="15,282 85,306 155,282 155,298 85,324 15,298"/></g><polygon points="20,30 150,30 150,270 85,294 20,270" fill="var(--panel)"/><line x1="85" y1="324" x2="85" y2="375" stroke="#8a8a8a"/><circle cx="85" cy="375" r="6" fill="var(--blue-light)" stroke="#8a8a8a"/></svg>
    <div class="badge"><div class="badge-core"><svg viewBox="0 0 32 32" fill="none" stroke="#fff" stroke-width="2"><circle cx="16" cy="14" r="9"/><circle cx="16" cy="14" r="5"/><circle cx="16" cy="14" r="1.5" fill="#fff"/><path d="M4 26h24"/></svg></div></div>
    <p class="text" style="top:90px"><strong>We are driven by a clear understanding of why we do what we do:</strong><br>To enrich lives, honour legacies and make a meaningful difference every day, for our residents, their families, our colleagues and our community</p>
    <div class="label" style="background:var(--blue)"><span class="initial" style="background:var(--blue-light)">P</span><span class="rest">urpose</span></div>
  </div>

  <div class="value warm" style="left:241px">
    <svg class="frame" viewBox="0 0 170 380"><g fill="var(--peach)"><polygon points="15,8 155,8 155,38 15,38"/><rect x="0" y="45" width="12" height="230"/><rect x="158" y="45" width="12" height="230"/><polygon points="15,282 85,306 155,282 155,298 85,324 15,298"/></g><polygon points="20,30 150,30 150,270 85,294 20,270" fill="var(--panel)"/><line x1="85" y1="324" x2="85" y2="375" stroke="#8a8a8a"/><circle cx="85" cy="375" r="6" fill="var(--peach-dark)" stroke="#8a8a8a"/></svg>
    <div class="badge"><div class="badge-core"><svg viewBox="0 0 32 32" fill="none" stroke="#fff" stroke-width="2"><path d="M16 4l9 4v8c0 6-4 9-9 12-5-3-9-6-9-12V8z"/><path d="M16 10l1.8 3.6 4 .6-2.9 2.8.7 4-3.6-1.9-3.6 1.9.7-4-2.9-2.8 4-.6z" fill="#fff" stroke="none"/></svg></div></div>
    <p class="text">We hold ourselves to the highest standards, delivering exceptional care and creating an environment where both residents &amp; staff can thrive.</p>
    <div class="label" style="background:var(--peach)"><span class="initial" style="background:var(--brown)">E</span><span class="rest">xcellence</span></div>
  </div>

  <div class="value cool" style="left:424px">
    <svg class="frame" viewBox="0 0 170 380"><g fill="var(--blue)"><polygon points="15,8 155,8 155,38 15,38"/><rect x="0" y="45" width="12" height="230"/><rect x="158" y="45" width="12" height="230"/><polygon points="15,282 85,306 155,282 155,298 85,324 15,298"/></g><polygon points="20,30 150,30 150,270 85,294 20,270" fill="var(--panel)"/><line x1="85" y1="324" x2="85" y2="375" stroke="#8a8a8a"/><circle cx="85" cy="375" r="6" fill="var(--blue-light)" stroke="#8a8a8a"/></svg>
    <div class="badge"><div class="badge-core"><svg viewBox="0 0 32 32" fill="none" stroke="#fff" stroke-width="2"><path d="M16 8c-3-2-7-2-10-1v16c3-1 7-1 10 1 3-2 7-2 10-1V7c-3-1-7-1-10 1z"/><path d="M16 8v16"/></svg></div></div>
    <p class="text">We build trust through honest, respectful communication, welcoming feedback, sharing ideas, and embracing change as a path to continuous growth.</p>
    <div class="label" style="background:var(--blue)"><span class="initial" style="background:var(--navy)">O</span><span class="rest">penness</span></div>
  </div>

  <div class="value warm" style="left:607px">
    <svg class="frame" viewBox="0 0 170 380"><g fill="var(--peach)"><polygon points="15,8 155,8 155,38 15,38"/><rect x="0" y="45" width="12" height="230"/><rect x="158" y="45" width="12" height="230"/><polygon points="15,282 85,306 155,282 155,298 85,324 15,298"/></g><polygon points="20,30 150,30 150,270 85,294 20,270" fill="var(--panel)"/><line x1="85" y1="324" x2="85" y2="375" stroke="#8a8a8a"/><circle cx="85" cy="375" r="6" fill="var(--peach-dark)" stroke="#8a8a8a"/></svg>
    <div class="badge"><div class="badge-core"><svg viewBox="0 0 32 32" fill="#fff"><path d="M16 3c1 5 8 8 8 16a8 8 0 0 1-16 0c0-4 2-6 3-8 1 3 2 4 3 4 0-4 0-8 2-12z"/></svg></div></div>
    <p class="text">We are passionate about delivering exceptional care. We take pride in what we do and in making a real difference in people’s lives.</p>
    <div class="label" style="background:var(--peach)"><span class="initial" style="background:var(--brown)">P</span><span class="rest">assion</span></div>
  </div>

  <div class="value cool" style="left:790px">
    <svg class="frame" viewBox="0 0 170 380"><g fill="var(--blue)"><polygon points="15,8 155,8 155,38 15,38"/><rect x="0" y="45" width="12" height="230"/><rect x="158" y="45" width="12" height="230"/><polygon points="15,282 85,306 155,282 155,298 85,324 15,298"/></g><polygon points="20,30 150,30 150,270 85,294 20,270" fill="var(--panel)"/><line x1="85" y1="324" x2="85" y2="375" stroke="#8a8a8a"/><circle cx="85" cy="375" r="6" fill="var(--blue-light)" stroke="#8a8a8a"/></svg>
    <div class="badge"><div class="badge-core"><svg viewBox="0 0 32 32" fill="none" stroke="#fff" stroke-width="2"><circle cx="22" cy="9" r="4"/><path d="M20 15h4M21 18h2"/><path d="M5 27h22M7 23h16v4H7z"/></svg></div></div>
    <p class="text">We are committed to personal and professional growth; empowering each other through ongoing development, reflection, and shared knowledge.</p>
    <div class="label" style="background:var(--blue)"><span class="initial" style="background:var(--navy)">L</span><span class="rest">earning</span></div>
  </div>

  <div class="value warm" style="left:973px">
    <svg class="frame" viewBox="0 0 170 380"><g fill="var(--peach-dark)"><polygon points="15,8 155,8 155,38 15,38"/><rect x="0" y="45" width="12" height="230"/><rect x="158" y="45" width="12" height="230"/><polygon points="15,282 85,306 155,282 155,298 85,324 15,298"/></g><polygon points="20,30 150,30 150,270 85,294 20,270" fill="var(--panel)"/><line x1="85" y1="324" x2="85" y2="375" stroke="#8a8a8a"/><circle cx="85" cy="375" r="6" fill="var(--peach-dark)" stroke="#8a8a8a"/></svg>
    <div class="badge"><div class="badge-core"><svg viewBox="0 0 32 32"><path d="M16 17s-6-4-6-8a3 3 0 0 1 6-1 3 3 0 0 1 6 1c0 4-6 8-6 8z" fill="#fff"/><path d="M4 22l6-2h7l-4 3M4 27l8-1 14-6" fill="none" stroke="#fff" stroke-width="2"/></svg></div></div>
    <p class="text">We actively listen and seek to understand before being understood, recognising the unique stories, feelings, &amp; needs of others.</p>
    <div class="label" style="background:var(--peach-dark)"><span class="initial" style="background:var(--brown)">E</span><span class="rest">mpathy</span></div>
  </div>

  <div class="footer-brand"><span class="mark"></span><span class="name">SOLENNE</span></div>
  <div class="divider"></div>
  <p class="web">solennehealthcare.co.uk</p>
</div>
</body>
</html>
```